Business Card & Logo Design

Originally the brief was for a card only - I now think it's probably better to include a logo design as well. PLease add $200 to the Budget of $210, Apologies for the inconvenience for thaos that have already submitted designs.

Lamp And Harbor Studios Pty Ltd is a video/dvd/ production company. Primarily corporate medium to high end. It's a one man operation that's been in business 20 years.

The name " Lamp and Harbor" is a primarily a reference to Lucien Marbeck film that's about film making. Shooting "Lamp and harbor" is also a technique employed by cinematographers to make scenes shot in daylight look like night.

See the design emphasising blue day/night tones but open to other ideas.

Main Text can either be Lamp and Harbor Studios or Lamp And Harbor.
Updates

Many thanks to all designers who submitted ideas for this brief.

Choosing between the designs was very difficult indeed.

I wish everyone the best and may the next job be yours!

Walter

Industry/Entity Type

Business

Requirements
Must have
• Text for card:
In Larger Print
Lamp And Harbor Studios or Lamp And Harbor
Walter Brenic
In Smaller Print
Lamp And Harbor Studios Pty Ltd.
17 Calder Lane
Glen Iris, VIC, 3146
P: 9734 2061
m: 0417 385 902
e: walterbrenic@examplemail.net

```html
<!DOCTYPE html>
<html lang="en">
<head>
<meta charset="utf-8">
<title>Walter Brenic – Lamp and Harbor Studios</title>
<link rel="stylesheet" href="https://fonts.googleapis.com/css2?family=Arimo:wght@400;700&display=swap">
<style>
  :root {
    --sky-deep: #0a5fb4;
    --sky-mid: #1f8fe0;
    --sky-light: #5cc3f5;
    --paper: #ffffff;
    --paper-shade: #eef4f9;
    --silver-top: #ffffff;
    --silver-bottom: #b9c3cc;
    --accent-blue: #1a78cc;
    --ink: #3a3a3a;
  }
  html, body {
    margin: 0;
    padding: 0;
    width: 1200px;
    height: 686px;
    overflow: hidden;
    background: #ffffff;
  }
  .card {
    position: relative;
    width: 1200px;
    height: 686px;
    overflow: hidden;
    font-family: "Arimo", Arial, sans-serif;
    background: var(--paper);
  }
  .card__backdrop {
    position: absolute;
    inset: 0;
  }
  .card__glow {
    position: absolute;
    left: 20px;
    top: 40px;
    width: 300px;
    height: 300px;
    border-radius: 50%;
    background: radial-gradient(circle, rgba(120,210,255,0.45) 0%, rgba(120,210,255,0.12) 55%, rgba(120,210,255,0) 72%);
  }
  .brand {
    position: absolute;
    top: 30px;
    left: 0;
    width: 1200px;
    display: flex;
    justify-content: center;
    align-items: center;
    gap: 12px;
    color: var(--paper);
    font-size: 24px;
    font-weight: 700;
    letter-spacing: 1px;
  }
  .brand__square {
    width: 22px;
    height: 22px;
    background: var(--paper);
  }
  .person-name {
    position: absolute;
    top: 130px;
    left: 0;
    width: 1200px;
    margin: 0;
    text-align: center;
    font-size: 122px;
    font-weight: 400;
    line-height: 1;
    letter-spacing: 1px;
    color: var(--silver-bottom);
    background: linear-gradient(180deg, var(--silver-top) 0%, #eef2f5 50%, var(--silver-bottom) 100%);
    -webkit-background-clip: text;
    background-clip: text;
    -webkit-text-fill-color: transparent;
    filter: drop-shadow(0 3px 3px rgba(0,40,90,0.35));
  }
  .company-name {
    position: absolute;
    top: 318px;
    left: 0;
    width: 1200px;
    margin: 0;
    text-align: center;
    font-size: 58px;
    font-weight: 400;
    line-height: 1;
    color: var(--paper);
  }
  .contact {
    position: absolute;
    left: 628px;
    top: 466px;
    margin: 0;
    font-style: normal;
    font-size: 26px;
    line-height: 42px;
    color: var(--ink);
  }
  .contact__company {
    color: var(--accent-blue);
  }
  .contact p { margin: 0; }
</style>
</head>
<body>
  <main class="card">
    <svg class="card__backdrop" width="1200" height="686" viewBox="0 0 1200 686" aria-hidden="true">
      <defs>
        <linearGradient id="sky" x1="0" y1="0" x2="1" y2="1">
          <stop offset="0" stop-color="#2aa0ea"/>
          <stop offset="0.55" stop-color="#1f8fe0"/>
          <stop offset="1" stop-color="#0a5fb4"/>
        </linearGradient>
        <linearGradient id="paper" x1="0" y1="0" x2="0" y2="1">
          <stop offset="0" stop-color="#eef4f9"/>
          <stop offset="0.3" stop-color="#ffffff"/>
        </linearGradient>
      </defs>
      <rect class="sky" width="1200" height="686" fill="url(#sky)"/>
      <path class="sky-highlight" d="M0 425 C 350 425, 750 385, 1200 290 L1200 350 C 750 420, 350 460, 0 490 Z" fill="#5cc3f5" opacity="0.45"/>
      <path class="paper" d="M0 490 C 350 460, 750 420, 1200 350 L1200 686 L0 686 Z" fill="url(#paper)"/>
    </svg>

    <div class="card__glow" role="img" aria-label="Soft glowing rings of light on the blue sky"></div>

    <div class="brand">
      <span class="brand__square"></span>
      <span class="brand__name">Lamp and Harbor</span>
    </div>

    <h1 class="person-name">Walter Brenic</h1>
    <h2 class="company-name">Lamp and Harbor Studios</h2>

    <address class="contact">
      <p class="contact__company">Lamp And Harbor Studios Pty Ltd.</p>
      <p>17 Calder Lane, Glen Iris, VIC, 3146</p>
      <p>Phone: 9734 2061</p>
      <p>Mobile: 0417 385 902</p>
      <p>E-Mail: walterbrenic@examplemail.net</p>
    </address>
  </main>
</body>
</html>
```